V9 Web Design Project

New company website for Intel cyber security company.

Style should be cool, but remain appropriate for very serious subject matter and audience.

Target Market(s)

Target audience is government and the military

Navigation needs to include:
- About Us
- Services
- Careers
- Contact Us
- Contracts

As well as 2 feature areas - use "Technology Integration" and "Case Study" as the supporting headlines.

Industry/Entity Type

Security

Font styles to use
Sans Serif

Colors

Designer to choose colors to be used in the design.

Requirements
Must have
• Mountain imagery and theme.

Use logo attached.

New Tagline - "Securing the Continuum"
Nice to have
• Supporting imagery could include photos representative of security - avoid cliches.
Should not have
• Needs to be serious not frivolous

```html
<!DOCTYPE html>
<html lang="en">
<head>
<meta charset="utf-8">
<title>V9 Group — Securing the Continuum</title>
<link rel="stylesheet" href="https://fonts.googleapis.com/css2?family=Mukta:wght@300;400;500&display=swap">
<style>
  :root {
    --blue: #3a97dd;
    --blue-line: #4a9fe0;
    --ink: #3d3d3d;
    --white: #ffffff;
    --band: #eeeeee;
    --hero-top: #6d7f98;
    --hero-mid: #3c5274;
    --hero-low: #2c3f5e;
  }
  * { margin: 0; padding: 0; box-sizing: border-box; }
  html, body { width: 1200px; height: 1000px; overflow: hidden; }
  body { font-family: "Mukta", Arial, sans-serif; font-weight: 300; color: var(--ink); background: var(--white); position: relative; }

  .hero { position: absolute; left: 0; top: 0; width: 1200px; height: 410px; overflow: hidden; }
  .hero-backdrop {
    position: absolute; inset: 0;
    background:
      radial-gradient(ellipse 420px 260px at 560px 200px, rgba(215,225,238,.55), transparent 70%),
      radial-gradient(ellipse 360px 200px at 1000px 120px, rgba(200,212,228,.45), transparent 70%),
      radial-gradient(ellipse 500px 180px at 800px 380px, rgba(190,205,225,.4), transparent 70%),
      linear-gradient(180deg, var(--hero-top) 0%, var(--hero-mid) 55%, var(--hero-low) 100%);
  }

  .brand { position: absolute; left: 68px; top: 22px; width: 187px; text-align: center; }
  .brand-plate { display: flex; align-items: center; gap: 8px; height: 47px; background: var(--white); padding: 0 10px; }
  .brand-square { width: 30px; height: 30px; background: var(--hero-mid); flex: none; }
  .brand-name { font-size: 26px; font-weight: 400; color: #1c2d6b; letter-spacing: .5px; line-height: 1; padding-top: 4px; }
  .tagline { margin-top: 12px; font-size: 14px; font-style: italic; color: var(--white); font-weight: 300; padding-left: 10px; }

  .main-nav a {
    position: absolute; top: 34px; font-size: 17px; color: var(--white); text-decoration: none;
    padding-bottom: 3px; border-bottom: 2px solid var(--blue-line); line-height: 22px;
  }

  .hero-copy { position: absolute; left: 0; top: 166px; width: 1200px; text-align: center; color: var(--white); font-size: 28px; line-height: 34px; font-weight: 300; }
  .hero-button {
    position: absolute; left: 532px; top: 251px; width: 136px; height: 43px;
    background: var(--blue); color: var(--white); border-radius: 3px;
    font-size: 16px; line-height: 44px; text-align: center; text-decoration: none;
  }
  .slider-dots { position: absolute; top: 365px; left: 574px; display: flex; gap: 8px; }
  .slider-dots span { width: 12px; height: 12px; border-radius: 50%; background: rgba(255,255,255,.55); }
  .slider-dots span.active { background: var(--white); }

  .intro { position: absolute; left: 0; top: 410px; width: 1200px; height: 207px; background: var(--band); text-align: center; }
  .intro-title { position: absolute; top: 34px; left: 0; width: 1200px; font-size: 31px; font-weight: 400; color: var(--blue); line-height: 40px; }
  .intro-rule { position: absolute; top: 54px; height: 2px; background: var(--blue-line); }
  .intro-text { position: absolute; top: 78px; left: 60px; width: 1080px; font-size: 30px; line-height: 38px; letter-spacing: 1.1px; color: #444; }

  .expertise { position: absolute; left: 21px; top: 658px; }
  .expertise h2 { font-size: 25px; font-weight: 400; color: var(--blue); line-height: 32px; }
  .expertise-list { position: absolute; top: 55px; left: 21px; list-style: none; width: 420px; }
  .expertise-list li { position: relative; height: 33px; font-size: 26px; line-height: 34px; padding-left: 36px; white-space: nowrap; color: #333; }
  .expertise-list svg { position: absolute; left: 5px; top: 9px; }
  .expertise-list li + li::before { content: ""; position: absolute; left: 0; top: 0; width: 26px; height: 1px; background: #bbb; }

  .divider { position: absolute; left: 599px; top: 678px; width: 2px; height: 160px; background: #555; }

  .profile { position: absolute; left: 600px; top: 658px; width: 600px; text-align: center; }
  .profile h2 { font-size: 25px; font-weight: 400; color: var(--blue); line-height: 32px; }
  .profile-rule { width: 94px; height: 2px; background: var(--blue-line); margin: 4px auto 0; }
  .profile p { margin-top: 20px; font-size: 25px; line-height: 33px; color: #333; }

  .site-footer { position: absolute; left: 0; top: 888px; width: 1200px; height: 112px; background: var(--band); text-align: center; }
  .site-footer p { margin-top: 41px; font-size: 19px; color: var(--blue); }
</style>
</head>
<body>
  <header class="hero">
    <div class="hero-backdrop" role="img" aria-label="Photograph of a snow-covered mountain ridge under a cloudy blue sky"></div>

    <div class="brand">
      <div class="brand-plate">
        <span class="brand-square"></span>
        <span class="brand-name">V9 GROUP</span>
      </div>
      <p class="tagline">Securing the Continuum</p>
    </div>

    <nav class="main-nav">
      <a href="#" style="left:560px">About us</a>
      <a href="#" style="left:668px">Services</a>
      <a href="#" style="left:776px">Careers</a>
      <a href="#" style="left:866px">Contact Us</a>
      <a href="#" style="left:992px">Contracts</a>
      <a href="#" style="left:1100px">Features</a>
    </nav>

    <p class="hero-copy">V9 Group helps clients achieve new heights by helping<br>them produce results and be more competitive.</p>
    <a class="hero-button" href="#">Learn More</a>
    <div class="slider-dots"><span class="active"></span><span></span><span></span></div>
  </header>

  <section class="intro">
    <span class="intro-rule" style="left:99px;width:201px"></span>
    <h1 class="intro-title">V9 Group helps clients achieve new heights</h1>
    <span class="intro-rule" style="left:908px;width:195px"></span>
    <p class="intro-text">V9 Group, Inc. is an independent consulting firm providing professional, technical and management solutions to leading global corporations and the federal government.</p>
  </section>

  <section class="expertise">
    <h2>V9 Group's major areas of expertise include :</h2>
  </section>
  <ul class="expertise-list" style="position:absolute;left:42px;top:713px">
    <li><svg width="16" height="16" viewBox="0 0 24 24"><path fill="#555" d="M12 2l3 7 7.5.6-5.7 5 1.8 7.4L12 18l-6.6 4 1.8-7.4-5.7-5L9 9z"/></svg>Technology Integration Solutions</li>
    <li><svg width="16" height="16" viewBox="0 0 24 24"><path fill="#555" d="M12 2l3 7 7.5.6-5.7 5 1.8 7.4L12 18l-6.6 4 1.8-7.4-5.7-5L9 9z"/></svg>National Defense Strategies</li>
    <li><svg width="16" height="16" viewBox="0 0 24 24"><path fill="#555" d="M12 2l3 7 7.5.6-5.7 5 1.8 7.4L12 18l-6.6 4 1.8-7.4-5.7-5L9 9z"/></svg>Information Security &amp; Protection</li>
    <li><svg width="16" height="16" viewBox="0 0 24 24"><path fill="#555" d="M12 2l3 7 7.5.6-5.7 5 1.8 7.4L12 18l-6.6 4 1.8-7.4-5.7-5L9 9z"/></svg>Tactics, Techniques and Procedures</li>
  </ul>

  <div class="divider"></div>

  <section class="profile">
    <h2>V9</h2>
    <div class="profile-rule"></div>
    <p>Our reputation is built on our professionalism, service, and<br>commitment to excellence. We employ the<br>latest technology to support our clients' needs and<br>offer solutions to improve efficiency and reduce costs.</p>
  </section>

  <footer class="site-footer">
    <p>© 2013 V9 Group Inc. - All Rights Reserved</p>
  </footer>
</body>
</html>
```